Heronby Mortgage Capital Business Card

We need a business card design for our mortgage servicing company. In addition to servicing the loans of homeowners, we help homeowners with purchasing their homes and any mortgage refinancing. We would like to see designs that use the colors in the logo attached below (gold-ish yellow and navy blue), and any other design you deem fit! The design should communicate a simpler life with smart mortgages provided by Heronby.

```html
<!DOCTYPE html>
<html lang="en">
<head>
<meta charset="utf-8">
<title>Heronby Mortgage Capital – Business Card</title>
<link rel="stylesheet" href="https://fonts.googleapis.com/css2?family=Open+Sans:wght@400;600;700&display=swap">
<style>
  :root {
    --bg: #222222;
    --card-white: #f4f4f4;
    --gold: #e0b23c;
    --gold-deep: #d4a22e;
    --navy: #231d57;
    --ink: #111111;
  }
  * { box-sizing: border-box; margin: 0; padding: 0; }
  html, body { width: 1200px; height: 780px; overflow: hidden; }
  body {
    background: var(--bg);
    font-family: "Open Sans", Arial, sans-serif;
    display: flex;
    align-items: center;
    justify-content: center;
    gap: 50px;
  }
  .card {
    position: relative;
    width: 525px;
    height: 300px;
    box-shadow: 0 12px 30px rgba(0,0,0,.45);
    overflow: hidden;
  }
  /* Front */
  .card-front { background: var(--card-white); }
  .brand {
    position: absolute;
    left: 40px;
    top: 70px;
    display: flex;
    align-items: center;
    gap: 10px;
    font-weight: 700;
    font-size: 38px;
    color: var(--gold);
    letter-spacing: .5px;
  }
  .brand-dot {
    width: 14px; height: 14px;
    border-radius: 50%;
    background: var(--navy);
  }
  .divider { position: absolute; inset: 0; }
  .details {
    position: absolute;
    left: 268px;
    top: 92px;
    color: var(--ink);
  }
  .person-name {
    font-weight: 700;
    font-size: 26px;
    line-height: 1.1;
    white-space: nowrap;
  }
  .person-name .first { color: var(--gold); }
  .person-name .last { color: var(--navy); }
  .person-title { font-size: 15px; margin-top: 2px; }
  .address { font-size: 13px; line-height: 1.4; margin-top: 8px; }
  .contact-list { list-style: none; margin-top: 6px; font-size: 13px; line-height: 1.45; }
  .contact-list li { display: flex; align-items: center; gap: 7px; }
  .contact-list svg { width: 12px; height: 12px; flex: none; fill: var(--gold); }

  /* Back */
  .card-back { background: var(--gold); }
  .back-pattern {
    position: absolute; inset: 0;
    background: linear-gradient(135deg, var(--gold-deep) 0%, var(--gold) 55%, #e8c25a 100%);
  }
  .back-brand {
    position: absolute;
    left: 50%;
    top: 58%;
    transform: translate(-50%, -50%);
    font-weight: 700;
    font-size: 22px;
    color: var(--navy);
  }
</style>
</head>
<body>
  <section class="card card-front" aria-label="Business card front">
    <div class="brand"><span class="brand-dot"></span>Heronby</div>
    <svg class="divider" width="525" height="300" viewBox="0 0 525 300" aria-hidden="true">
      <line x1="300" y1="30" x2="190" y2="270" stroke="var(--navy)" stroke-width="1"/>
    </svg>
    <div class="details">
      <p class="person-name"><span class="first">Lenka</span> <span class="last">Dvorakova</span></p>
      <p class="person-title">Managing Director</p>
      <p class="address">1480 Alder Bend Rd. Suite 310<br>Denton, TX 76201</p>
      <ul class="contact-list">
        <li><svg viewBox="0 0 24 24" aria-hidden="true"><path d="M6.6 10.8a15.1 15.1 0 0 0 6.6 6.6l2.2-2.2c.3-.3.7-.4 1-.2 1.1.4 2.3.6 3.6.6.6 0 1 .4 1 1V20c0 .6-.4 1-1 1A17 17 0 0 1 3 4c0-.6.4-1 1-1h3.5c.6 0 1 .4 1 1 0 1.3.2 2.5.6 3.6.1.3 0 .7-.2 1z"/></svg>(940) 555-0142</li>
        <li><svg viewBox="0 0 24 24" aria-hidden="true"><path d="M2 5h20v14H2zm2 2v.5l8 5 8-5V7l-8 5z"/></svg>info@heronbymortgage.com</li>
        <li><svg viewBox="0 0 24 24" aria-hidden="true"><path d="M12 2a10 10 0 1 0 0 20 10 10 0 0 0 0-20zm6.9 9h-3a15 15 0 0 0-1.3-6A8 8 0 0 1 18.9 11zM12 4c.9 1.3 1.7 3.8 1.9 7h-3.8c.2-3.2 1-5.7 1.9-7zM9.4 5a15 15 0 0 0-1.3 6h-3A8 8 0 0 1 9.4 5zM5.1 13h3a15 15 0 0 0 1.3 6 8 8 0 0 1-4.3-6zM12 20c-.9-1.3-1.7-3.8-1.9-7h3.8c-.2 3.2-1 5.7-1.9 7zm2.6-1a15 15 0 0 0 1.3-6h3a8 8 0 0 1-4.3 6z"/></svg>www.heronbymortgage.com</li>
      </ul>
    </div>
  </section>

  <section class="card card-back" aria-label="Business card back">
    <div class="back-pattern" role="img" aria-label="Repeating brand pattern in darker gold and white tones across the card back"></div>
    <p class="back-brand">Heronby</p>
  </section>
</body>
</html>
```